Dishwave Site

I would like to do a blog for food lovers. The name of the blog is WaveDish. I want to build something like Marcus Thelwell and Gerald Fennimore. Something cool and different. In this blog i need: Place for pictures, videos, instagram connection, Facebook Linked to see fans wich like the blog on Facebook....

Reason: I need more options of design.

Requirements
Nice to have
• - Facebook link
- Instagram
- Something with foursquare

```html
<!DOCTYPE html>
<html lang="en">
<head>
<meta charset="utf-8">
<title>Dishwave</title>
<link href="https://fonts.googleapis.com/css2?family=Advent+Pro:wght@300;400&family=Arimo:ital,wght@0,400;1,400&display=swap" rel="stylesheet">
<style>
:root{
  --bg:#f1efeb;
  --panel:#f7f6f3;
  --blue:#1ec1ee;
  --blue-dark:#0f9cc9;
  --blue-light:#31cdf5;
  --pink:#e8157a;
  --text:#2b2b2b;
  --muted:#666;
  --line:#d9d6d0;
  --white:#fff;
}
*{margin:0;padding:0;box-sizing:border-box}
html,body{width:1107px;height:1200px;overflow:hidden}
body{background:var(--bg);font-family:"Arimo",Arial,sans-serif;color:var(--text);position:relative}
.abs{position:absolute}
.display{font-family:"Advent Pro",sans-serif;font-weight:300;text-transform:uppercase}

.contact{left:140px;top:16px;font-size:11.5px;color:#555;line-height:18px}
.contact .row{display:flex;align-items:center;gap:6px}
.search{left:767px;top:20px;width:197px;height:25px;border:1px solid #ccc;background:#fafafa;font-size:11px;color:#aaa;padding:6px 6px}
.search svg{position:absolute;right:5px;top:4px}

.band{left:0;top:80px;width:1107px;height:45px;background:linear-gradient(var(--blue-light),var(--blue))}
.panel{left:116px;top:111px;width:875px;height:1089px;background:var(--panel);box-shadow:0 0 14px rgba(0,0,0,.08)}
.navbar{left:97px;top:66px;width:913px;height:45px;background:linear-gradient(#27c9f3,var(--blue))}
.fold-l{left:97px;top:111px;width:0;height:0;border-top:12px solid var(--blue-dark);border-left:19px solid transparent}
.fold-r{left:991px;top:111px;width:0;height:0;border-top:12px solid var(--blue-dark);border-right:19px solid transparent}
.nav{left:0;top:66px;width:1107px;height:45px}
.nav a{color:var(--white);text-decoration:none;font-size:18px;position:absolute;top:13px;line-height:20px}
.nav a.active::after{content:"";position:absolute;left:-11px;right:-20px;bottom:-12px;height:4px;background:var(--pink)}

.logo{left:450px;top:9px;width:207px;height:179px;background:var(--white);border:1px solid #ccc;box-shadow:0 1px 3px rgba(0,0,0,.15);text-align:center}
.logo .word{position:absolute;left:0;right:0;top:120px;font-size:44px;line-height:50px;color:#333;letter-spacing:1px}

.slider{left:141px;top:139px;width:823px;height:360px;background:var(--white);box-shadow:0 1px 3px rgba(0,0,0,.15)}
.slide-photo{left:145px;top:143px;width:815px;height:352px;background:radial-gradient(ellipse at 45% 55%,#b6402c 0%,#8a3b26 25%,#d4a66b 55%,#e8d2a8 80%,#cfc3b0 100%)}
.caption{left:145px;top:405px;width:815px;height:90px;background:rgba(40,30,25,.55);color:var(--white);padding:10px 16px}
.caption h2{font-family:"Advent Pro",sans-serif;font-weight:300;font-size:21px;margin-bottom:6px}
.caption p{font-size:11px;line-height:16.5px}
.arrow{top:300px}

.rule{height:1px;background:var(--line)}
.welcome-title{left:145px;width:815px;top:533px;text-align:center;font-size:29px;color:var(--blue)}
.welcome-text{left:150px;width:805px;top:575px;text-align:center;font-size:11.2px;line-height:17px}
.welcome-sign{right:147px;top:616px;font-size:13px;font-style:italic;color:var(--blue)}

.date{left:140px;top:673px}
.date .mon{position:absolute;left:23px;top:0;font-size:10px;color:#333}
.date .day{position:absolute;left:24px;top:15px;font-size:26px;color:#222}
.date .yr{position:absolute;left:36px;top:52px;font-size:10px;color:#333}
.post-title{left:242px;top:672px;width:470px;font-size:23px;line-height:24px;color:var(--blue)}
.post-meta{left:242px;top:724px;font-size:11.5px;color:#222}
.post-meta em{font-style:normal;color:var(--pink)}
.like{left:658px;top:720px;width:35px;height:16px;border:1px solid #ccd;background:#eef0f6;font-size:9.5px;color:#334;display:flex;align-items:center;gap:2px;padding-left:2px}
.like i{width:8px;height:8px;background:#3b5a9a;display:block}
.post-photo{left:141px;top:748px;width:551px;height:272px;border:2px solid var(--white);background:radial-gradient(ellipse at 45% 60%,#b9492f 0%,#8c5a3d 30%,#d2b067 55%,#4d8d8f 80%,#3d6f73 100%)}
.post-body{left:141px;top:1032px;width:552px;font-size:12px;line-height:20.3px}
.more{left:139px;top:1143px;width:103px;height:35px;background:var(--blue);color:var(--white);font-size:17px;text-align:center;line-height:35px}

.ad{left:710px;top:676px;width:254px;height:211px;background:linear-gradient(135deg,#3a3a3a,#1c1c1c 55%,#5a1a1f)}
.side-head{left:712px;top:907px;display:flex;align-items:center;gap:10px;font-size:25px;color:var(--blue)}
.video{left:719px;top:965px;width:245px;height:203px;border:1px solid #ccc;background:linear-gradient(160deg,#8a5a33,#c7995f 45%,#3c3836)}
.video-bar{left:720px;top:1148px;width:243px;height:19px;background:linear-gradient(#fafafa,#ddd);border-top:1px solid #bbb}
</style>
</head>
<body>

<div class="abs band"></div>
<div class="abs panel"></div>
<div class="abs navbar"></div>
<div class="abs fold-l"></div>
<div class="abs fold-r"></div>

<div class="abs contact">
  <div class="row"><svg width="14" height="10"><rect width="14" height="10" fill="#1ec1ee"/><path d="M0 0 L7 6 L14 0" stroke="#fff" fill="none"/></svg>contact@dishwave.domain_name</div>
  <div class="row"><svg width="14" height="14"><circle cx="7" cy="7" r="7" fill="#1ec1ee"/><path d="M4.5 4 q0 6 5 6" stroke="#fff" stroke-width="2" fill="none"/></svg>+231 0800 55120 , +21 300 418</div>
</div>
<div class="abs search">search<svg width="16" height="16"><circle cx="6.5" cy="6.5" r="4.5" stroke="#1ec1ee" stroke-width="2.5" fill="none"/><path d="M10 10 L15 15" stroke="#1ec1ee" stroke-width="3"/></svg></div>

<nav class="abs nav display">
  <a class="active" href="#" style="left:138px">Home</a>
  <a href="#" style="left:215px">About</a>
  <a href="#" style="left:294px">Items</a>
  <a href="#" style="left:376px">Party</a>
  <a href="#" style="left:686px">Shop</a>
  <a href="#" style="left:758px">Staff</a>
  <a href="#" style="left:839px">FAQ</a>
  <a href="#" style="left:905px">Contact</a>
</nav>

<div class="abs slider"></div>
<div class="abs slide-photo" role="img" aria-label="Close-up photo of a grilled sandwich with roasted peppers, olives and basil"></div>
<div class="abs caption">
  <h2>Lorem ipsum dolor sit amet, consectetur</h2>
  <p>Nulla malesuada ullamcorper cursus. Vivamus fermentum sollicitudin sodales. Aliquam odio magna, hendrerit id ultricies vitae, auctor vitae purus. Nunc pellentesqu.</p>
</div>
<svg class="abs arrow" style="left:104px" width="26" height="44"><path d="M22 2 L4 22 L22 42" stroke="#c8c8c8" stroke-width="6" fill="none"/></svg>
<svg class="abs arrow" style="left:978px" width="26" height="44"><path d="M4 2 L22 22 L4 42" stroke="#c8c8c8" stroke-width="6" fill="none"/></svg>

<div class="abs logo">
  <div class="word display">Dishwave</div>
</div>

<div class="abs rule" style="left:145px;top:521px;width:815px"></div>
<div class="abs rule" style="left:307px;top:525px;width:492px"></div>
<h1 class="abs welcome-title display">Welcome to Dishwave</h1>
<p class="abs welcome-text">Lorem ipsum dolor sit amet, consectetur adipiscing elit. Nunc id porttitor nibh. Cras vel vestibulum velit. Vivamus placerat est non erat scelerisque quis fermentum turpis consequat. Vestibulum non ornare odio. Suspendisse potenti. Proin feugiat accumsan fermentum. Suspendisse eget aliquam nisl.</p>
<div class="abs welcome-sign">-- Website Owner Name, Country Name</div>
<div class="abs rule" style="left:145px;top:646px;width:815px"></div>
<div class="abs rule" style="left:307px;top:642px;width:492px"></div>

<div class="abs date">
  <svg class="abs" style="left:0;top:0" width="16" height="62"><path d="M2 0 V20 Q2 28 8 29 Q14 28 14 20 V0" stroke="#777" stroke-width="2" fill="none"/><path d="M6 0 V18 M10 0 V18" stroke="#777" stroke-width="2"/><rect x="6" y="28" width="4" height="34" fill="#777"/></svg>
  <div class="mon">OCTOBER</div>
  <div class="day">21st</div>
  <div class="yr">2012</div>
</div>
<h2 class="abs post-title display">Nullam auctor faucibus sem, a placerat onef augue</h2>
<div class="abs post-meta"><em>Postd in:</em> Staff &nbsp; <em>Tags:</em> resturant, food, lorem ipsum</div>
<div class="abs like"><i></i>Like</div>
<div class="abs post-photo" role="img" aria-label="Photo of stir-fried noodles with chicken, mushrooms, red peppers and spring onion on a teal plate"></div>
<p class="abs post-body">Vestibulum arcu odio, adipiscing eget bibendum et, vulputate non felis. Etiam condimentum diam vitae ante placerat dapibus. Mauris molestie nisl at enim blandit eleifend. In laoreet justo in magna commodo ac malesuada neque porta. Proin magna leo, commodo sit amet luctus sed, rhoncus quis felis. Mauris sollicitudin convallis urna in pharetra. Quisque id erat velit, vel ornare tellus. Morbi vitae ligula mauris. Sed at ante non nisi ornare tincidunt id ut augue.</p>
<div class="abs more display">Read more</div>
<div class="abs rule" style="left:141px;top:1193px;width:552px"></div>

<div class="abs ad" role="img" aria-label="Advertisement banner showing an outdoor backpack"></div>
<div class="abs side-head display">
  <svg width="32" height="32"><circle cx="16" cy="16" r="15" stroke="#1ec1ee" stroke-width="1.5" fill="none"/><circle cx="16" cy="16" r="10" stroke="#1ec1ee" stroke-width="2" fill="none"/><path d="M10 10 L22 22 M22 10 L10 22" stroke="#1ec1ee" stroke-width="2"/></svg>
  Latest Vedio
</div>
<div class="abs rule" style="left:710px;top:946px;width:254px"></div>
<div class="abs video" role="img" aria-label="Video thumbnail of a cooking show in a kitchen"></div>
<div class="abs video-bar">
  <svg width="243" height="19"><circle cx="12" cy="9" r="6" fill="#bbb"/><rect x="28" y="8" width="140" height="3" fill="#999"/><circle cx="40" cy="9.5" r="3.5" fill="#777"/><text x="173" y="12" font-size="7" fill="#666" font-family="Arial, sans-serif">02:29</text><rect x="200" y="6" width="6" height="6" fill="#aaa"/><rect x="210" y="8" width="25" height="2" fill="#aaa"/></svg>
</div>
<div class="abs rule" style="left:710px;top:1196px;width:254px"></div>

</body>
</html>
```